Tovenly Website Redesign

We have a web site called tovenly.com that is all about education/information about legal marijuana. We're looking to significantly improve the modern-ness and look/feel of the web site - and to make it look like many of the best web sites out there today.

The task will be to come up with a better design for:
- The home page: http://tovenly.com/
- The logo (see the logo at the top of each page)
- The header and footer (for all the pages)
- The vaporizer page: http://tovenly.com/collections/vaporizer
- The store map page: http://tovenly.com/pages/shop-marijuana-in-colorado-state

The output of the project will be:
- screenshots of the designs and any images needed
- PSD file

Key requirements:
- Style needs to look fresh/modern
- Especially on the vaporizers page, the key things we want to drive is conversion - getting more people to interact with the page and actually click on the links to purchase vaporizers

Reason: Raised the budget and want to give designers a few more days to provide entries.

Note I clarified that I don't need code (HTML or CSS) for the project. I just need the designs, including images and the PSD file. Thanks.

Reason: We're getting closet to selecting a design, just need a few more days to iterate on a few we're working on.

Industry/Entity Type

Education

Font styles to use
Sans Serif

Requirements
Must have
• Must look like a modern/clean/fresh looking website design.

```html
<!DOCTYPE html>
<html lang="en">
<head>
<meta charset="utf-8">
<title>Tovenly – Shop marijuana in style</title>
<link href="https://fonts.googleapis.com/css2?family=Arimo:wght@400;700&family=Ubuntu:wght@400;500;700&display=swap" rel="stylesheet">
<style>
:root{
  --leaf-deep:#0f3d06;
  --leaf:#2f7d12;
  --leaf-bright:#4fa41f;
  --leaf-light:#8fcf55;
  --band:#1f7a0c;
  --nav-active:#175a0a;
  --dark:#141414;
  --dark-2:#1f1f1f;
  --button:#1f7f0c;
  --white:#ffffff;
  --ink:#111111;
  --muted:#e4e4e4;
  --star:#f4c20d;
  --stripe:#d9d9d9;
  --footer:#0c2a06;
}
*{box-sizing:border-box;margin:0;padding:0}
html,body{width:726px;height:1200px;overflow:hidden;background:var(--white)}
body{position:relative;font-family:"Arimo",Arial,sans-serif;color:var(--ink)}
.abs{position:absolute}

/* Hero header */
.hero{left:0;top:0;width:726px;height:257px;
  background:radial-gradient(ellipse at 62% 35%,var(--leaf-light) 0%,var(--leaf-bright) 25%,var(--leaf) 55%,var(--leaf-deep) 100%)}
.brand{left:73px;top:22px;width:267px;height:32px;background:var(--white);display:flex;align-items:center;padding-left:6px;gap:8px}
.brand-name{font-size:27px;font-weight:700;color:var(--leaf);letter-spacing:.5px}
.brand-tag{font-size:9.5px;color:var(--ink)}
.follow{left:580px;top:22px;width:73px;height:35px;background:var(--white);text-align:center;padding-top:4px}
.follow-label{font-size:8.5px;font-weight:700;letter-spacing:.3px}
.follow-icons{display:flex;justify-content:center;gap:11px;margin-top:4px}
.sq{width:12px;height:12px;border-radius:2px}
.sq.one{background:#3b5a98}.sq.two{background:#3aa9e0}
.slide-arrow{top:101px;width:30px;height:30px}
.hero-title{left:0;top:87px;width:726px;text-align:center;color:var(--white);font-size:30px;font-weight:700;letter-spacing:2.6px}
.hero-sub{left:0;top:132px;width:726px;text-align:center;color:var(--white);font-size:12.5px;font-weight:700;letter-spacing:1.2px}
.nav-rule{left:73px;top:207px;width:580px;height:1px;background:rgba(255,255,255,.25)}
.nav{left:112px;top:210px;height:47px;display:flex}
.nav a{display:flex;align-items:center;height:47px;padding:0 13px;color:var(--white);text-decoration:none;font-size:13px;font-weight:700;letter-spacing:.7px}
.nav a.active{background:var(--nav-active);padding:0 15px}
.nav .caret{font-size:6px;margin-left:4px}
.green-band{left:0;top:257px;width:726px;height:6px;background:var(--band)}
.band-notch{left:356px;top:263px}

/* Articles */
.articles{left:0;top:263px;width:726px;height:355px;background:linear-gradient(90deg,var(--dark) 0%,var(--dark-2) 50%,var(--dark) 100%)}
.article{width:279px;height:74px}
.article.right{width:275px}
.article-photo{left:0;top:0;width:70px;height:54px}
.article-title{left:77px;top:0;right:0;text-align:center;color:var(--white);font-size:8px;line-height:10px;font-weight:400}
.article-title.single{white-space:nowrap;font-size:7.8px;letter-spacing:-.05px}
.article-text{left:76px;right:0;color:var(--muted);font-size:5.6px;line-height:7.4px;text-align:justify}
.btn{right:0;top:59px;width:42px;height:13px;background:var(--button);color:var(--white);font-size:5.6px;display:flex;align-items:center;justify-content:center}

/* Section headings */
.section-title{left:75px;font-size:16.5px;font-weight:700;letter-spacing:1.5px;color:var(--ink)}
.stripes{height:6px;background:repeating-linear-gradient(0deg,var(--stripe) 0 1px,transparent 1px 2px)}

/* Products */
.products{left:0;top:693px;width:726px;height:150px;
  background:radial-gradient(ellipse at 60% 40%,var(--leaf-light) 0%,var(--leaf-bright) 30%,var(--leaf) 65%,var(--leaf-deep) 100%)}
.product{top:15px;width:105px}
.product-photo{width:105px;height:90px;position:relative;overflow:hidden}
.sale{position:absolute;right:0;top:0}
.price{margin-top:12px;text-align:center;color:var(--white);font-size:6.5px;font-weight:700}
.stars{margin-top:3px;display:flex;justify-content:center;gap:1px}

/* Blog */
.post{width:260px;height:80px}
.avatar{left:0;top:0;width:76px;height:76px;border-radius:50%;background:linear-gradient(160deg,#c9c9c9,#7d7d7d)}
.post-name{left:94px;top:9px;font-size:8.5px;font-weight:700;color:var(--ink)}
.post-text{left:94px;top:23px;width:164px;font-size:6.2px;line-height:12.3px;font-weight:700;text-align:justify;color:var(--ink)}

/* Footer */
.footer{left:0;top:1053px;width:726px;height:147px;font-family:"Ubuntu",Arial,sans-serif;
  background:radial-gradient(ellipse at 55% 40%,#2c6a12 0%,#17420a 40%,var(--footer) 100%);color:var(--white)}
.footer h4{font-size:8.5px;font-weight:500;margin-bottom:5px}
.footer p,.footer li{font-size:6.4px;line-height:11px;font-weight:500;list-style:none}
.social{display:flex;align-items:center;gap:8px;font-size:7px;margin-top:7px;margin-left:19px}
.social .sq{width:13px;height:13px}
.footer .legal{font-size:4.5px;line-height:6px;color:#b8c9b0}
</style>
</head>
<body>

<header class="abs hero" role="img" aria-label="Blurred green cannabis leaf photograph">
</header>
<div class="abs brand"><span class="brand-name">Tovenly</span><span class="brand-tag">Shop marijuana in style</span></div>
<div class="abs follow">
  <div class="follow-label">Fallow us on</div>
  <div class="follow-icons"><span class="sq one"></span><span class="sq two"></span></div>
</div>
<svg class="abs slide-arrow" style="left:73px" viewBox="0 0 30 30"><circle cx="15" cy="15" r="13.5" fill="none" stroke="#e6f2dc" stroke-width="2"/><path d="M17 9l-6 6 6 6" fill="none" stroke="#e6f2dc" stroke-width="2.5"/></svg>
<svg class="abs slide-arrow" style="left:623px" viewBox="0 0 30 30"><circle cx="15" cy="15" r="13.5" fill="none" stroke="#e6f2dc" stroke-width="2"/><path d="M13 9l6 6-6 6" fill="none" stroke="#e6f2dc" stroke-width="2.5"/></svg>
<h1 class="abs hero-title">Welcome To Tovenly</h1>
<p class="abs hero-sub">Shop marijuna in style</p>
<div class="abs nav-rule"></div>
<nav class="abs nav">
  <a class="active" href="#">Home</a>
  <a href="#">Blog</a>
  <a href="#">Marijuna 101</a>
  <a href="#">Legal Marijuna<span class="caret">▼</span></a>
  <a href="#">Vaporizers<span class="caret">▼</span></a>
</nav>
<div class="abs green-band"></div>

<section class="abs articles">
  <article class="abs article" style="left:73px;top:37px">
    <div class="abs article-photo" role="img" aria-label="Man smoking a joint" style="background:linear-gradient(135deg,#3a2a22,#b99a86)"></div>
    <h3 class="abs article-title" style="top:2px">Denver Man Admits Smoking Weed Was More Fun<br>When It Was Illegal</h3>
    <p class="abs article-text" style="top:30px">Jared Colby, a marijuana enthusiast living in the Denver area, told reporters Wednesday that he en yed getting high more when it was illegal.</p>
    <span class="abs btn">View Details</span>
  </article>
  <article class="abs article right" style="left:379px;top:37px">
    <div class="abs article-photo" role="img" aria-label="Chocolate brownies" style="background:linear-gradient(135deg,#4a1f12,#8a4a2e)"></div>
    <h3 class="abs article-title single" style="top:4px">The Best Ways To Take Marijuana (And Their Effects)</h3>
    <p class="abs article-text" style="top:22px">There are many ways to get high and a lot of them have different effects. So here's our list of the best ways to get high and the different ways you'll feel it.</p>
    <span class="abs btn">View Details</span>
  </article>
  <article class="abs article" style="left:73px;top:144px">
    <div class="abs article-photo" role="img" aria-label="Hands holding cannabis buds" style="background:linear-gradient(135deg,#c9a48a,#6e7a4a)"></div>
    <h3 class="abs article-title" style="top:2px">Six Ways To Improve Your High</h3>
    <p class="abs article-text" style="top:20px">Getting high on marijuana is wonderful, but there are a few little annoyances we all notice after we've done it a few times. Here's a six hacks to make your high as enjoyable and irritation free as possible.</p>
    <span class="abs btn">View Details</span>
  </article>
  <article class="abs article right" style="left:379px;top:144px">
    <div class="abs article-photo" role="img" aria-label="Hands holding a jar of buds" style="background:linear-gradient(135deg,#8a6a50,#5a6a3a)"></div>
    <h3 class="abs article-title" style="top:0">The 6 Best Ways to Store Your Weed</h3>
    <p class="abs article-text" style="top:18px">There's nothing worse than opening up your stash and finding out that your weed is completely dried out and stale. To help protect your weed and keep it fresh for longer, here are the best storage</p>
    <span class="abs btn">View Details</span>
  </article>
  <article class="abs article" style="left:73px;top:250px">
    <div class="abs article-photo" role="img" aria-label="Cannabis buds on white" style="background:linear-gradient(135deg,#f0f0f0,#8fa060)"></div>
    <h3 class="abs article-title" style="top:2px">The States Most Likely To Legalize Weed Next</h3>
    <p class="abs article-text" style="top:20px">If you live in the United States anywhere other than Colorado or Washington State then you're pretty screwed as far as legal marijuana goes. But never fear! Here are the states most likely to legalize weed next.</p>
    <span class="abs btn">View Details</span>
  </article>
  <article class="abs article right" style="left:379px;top:250px">
    <div class="abs article-photo" role="img" aria-label="Prison cell scenes" style="background:linear-gradient(90deg,#5a5a5a,#a04030 45%,#6a6a6a)"></div>
    <h3 class="abs article-title" style="top:3px">Five Of The Most Unfair Marijuana Sentences</h3>
    <p class="abs article-text" style="top:21px">In 48 states in America recreational marijuana use is still illegal. Over this time countless people have received completely over the top sentences for non-violent marijuana offences, but these five really are something else.</p>
    <span class="abs btn">View Details</span>
  </article>
</section>
<svg class="abs band-notch" width="14" height="9" viewBox="0 0 14 9"><path d="M0 0h14L7 8z" fill="#1f7a0c"/></svg>

<h2 class="abs section-title" style="top:660px">Vaporizers Products</h2>
<div class="abs stripes" style="left:267px;top:667px;width:459px"></div>

<section class="abs products" role="img" aria-label="Blurred green leaf background">
</section>
<svg class="abs" style="left:35px;top:744px" width="14" height="24" viewBox="0 0 14 24"><path d="M12 2L2 12l10 10" fill="none" stroke="#fff" stroke-width="2"/></svg>
<svg class="abs" style="left:673px;top:744px" width="14" height="24" viewBox="0 0 14 24"><path d="M2 2l10 10L2 22" fill="none" stroke="#fff" stroke-width="2"/></svg>

<div class="abs product" style="left:73px;top:708px">
  <div class="product-photo" role="img" aria-label="Wooden box vaporizer" style="background:linear-gradient(135deg,#e8d3a0,#b89a5a)">
    <svg class="sale" width="40" height="40" viewBox="0 0 40 40"><path d="M0 0h40v40z" fill="#000"/><text x="27" y="15" fill="#fff" font-size="6" font-weight="700" font-family="Arimo,sans-serif" transform="rotate(45 27 15)" text-anchor="middle">SALE</text></svg>
  </div>
  <p class="price">$119.00</p>
  <div class="stars"><svg width="50" height="9" viewBox="0 0 50 9"><g fill="#f4c20d"><path id="s" d="M4.5 0l1.3 2.9 3.2.3-2.4 2.1.7 3.1-2.8-1.6-2.8 1.6.7-3.1L0 3.2l3.2-.3z"/><use href="#s" x="10"/><use href="#s" x="20"/><use href="#s" x="30"/></g><use href="#s" x="40" fill="#fff"/></svg></div>
</div>
<div class="abs product" style="left:191px;top:708px">
  <div class="product-photo" role="img" aria-label="Desktop digital vaporizer" style="background:linear-gradient(180deg,#fff 20%,#d4d4d4 55%,#222 90%)">
    <svg class="sale" width="40" height="40" viewBox="0 0 40 40"><path d="M0 0h40v40z" fill="#000"/><text x="27" y="15" fill="#fff" font-size="6" font-weight="700" font-family="Arimo,sans-serif" transform="rotate(45 27 15)" text-anchor="middle">SALE</text></svg>
  </div>
  <p class="price">$239.00</p>
  <div class="stars"><svg width="50" height="9" viewBox="0 0 50 9"><g fill="#f4c20d"><use href="#s"/><use href="#s" x="10"/><use href="#s" x="20"/><use href="#s" x="30"/><use href="#s" x="40"/></g></svg></div>
</div>
<div class="abs product" style="left:310px;top:708px">
  <div class="product-photo" role="img" aria-label="Conical steel vaporizer" style="background:linear-gradient(180deg,#fff 15%,#9a9a9a 55%,#3a3a3a 95%)">
    <svg class="sale" width="40" height="40" viewBox="0 0 40 40"><path d="M0 0h40v40z" fill="#000"/><text x="27" y="15" fill="#fff" font-size="6" font-weight="700" font-family="Arimo,sans-serif" transform="rotate(45 27 15)" text-anchor="middle">SALE</text></svg>
  </div>
  <p class="price">$539.00</p>
  <div class="stars"><svg width="50" height="9" viewBox="0 0 50 9"><g fill="#f4c20d"><use href="#s"/><use href="#s" x="10"/><use href="#s" x="20"/><use href="#s" x="30"/><use href="#s" x="40"/></g></svg></div>
</div>
<div class="abs product" style="left:430px;top:708px">
  <div class="product-photo" role="img" aria-label="Portable handheld vaporizers" style="background:linear-gradient(90deg,#2a2a2a,#4a6a50 50%,#2a2a2a)">
    <svg class="sale" width="40" height="40" viewBox="0 0 40 40"><path d="M0 0h40v40z" fill="#000"/><text x="27" y="15" fill="#fff" font-size="6" font-weight="700" font-family="Arimo,sans-serif" transform="rotate(45 27 15)" text-anchor="middle">SALE</text></svg>
  </div>
  <p class="price">$199.00</p>
  <div class="stars"><svg width="50" height="9" viewBox="0 0 50 9"><g fill="#f4c20d"><use href="#s"/><use href="#s" x="10"/><use href="#s" x="20"/><use href="#s" x="30"/></g><use href="#s" x="40" fill="#fff"/></svg></div>
</div>
<div class="abs product" style="left:549px;top:708px">
  <div class="product-photo" role="img" aria-label="Wand vaporizer with charger" style="background:linear-gradient(90deg,#fff 20%,#333 50%,#fff 80%)">
    <svg class="sale" width="40" height="40" viewBox="0 0 40 40"><path d="M0 0h40v40z" fill="#000"/><text x="27" y="15" fill="#fff" font-size="6" font-weight="700" font-family="Arimo,sans-serif" transform="rotate(45 27 15)" text-anchor="middle">SALE</text></svg>
  </div>
  <p class="price">$135.00</p>
  <div class="stars"><svg width="50" height="9" viewBox="0 0 50 9"><g fill="#f4c20d"><use href="#s"/><use href="#s" x="10"/><use href="#s" x="20"/><use href="#s" x="30"/></g><use href="#s" x="40" fill="#fff"/></svg></div>
</div>

<h2 class="abs section-title" style="left:73px;top:883px">Recent Blog</h2>
<div class="abs stripes" style="left:189px;top:891px;width:464px"></div>

<article class="abs post" style="left:100px;top:920px">
  <div class="abs avatar" role="img" aria-label="Author portrait"></div>
  <h3 class="abs post-name">Marla Quent</h3>
  <p class="abs post-text">Lorem Ipsum is simply dummy text of the printing and typesetting industry. Lorem Ipsum has been the industry's standard dummy text ever since the 1500s, when an unknown printer took a galley of type</p>
</article>
<article class="abs post" style="left:381px;top:920px">
  <div class="abs avatar" role="img" aria-label="Author portrait"></div>
  <h3 class="abs post-name">Marla Quent</h3>
  <p class="abs post-text">Lorem Ipsum is simply dummy text of the printing and typesetting industry. Lorem Ipsum has been the industry's standard dummy text ever since the 1500s, when an unknown printer took a galley of type</p>
</article>

<footer class="abs footer" role="img" aria-label="Blurred dark green leaf background">
  <div class="abs" style="left:164px;top:39px;width:102px">
    <h4>Address</h4>
    <p>Lorem Ipsum is simply dummy text of the printing and typeset-ting industry<br>Phone: +1234567890<br>Email: Lorem Ipsum is simply</p>
  </div>
  <div class="abs" style="left:344px;top:39px">
    <h4>Important Links</h4>
    <ul><li>Home</li><li>Blog</li><li>Marijuna 101</li><li>Legal Marijuna</li><li>Voporizers</li></ul>
  </div>
  <div class="abs" style="left:470px;top:39px">
    <h4>Fallow Us On</h4>
    <div class="social"><span class="sq one"></span>Friendline</div>
    <div class="social"><span class="sq two"></span>Chirpnet</div>
  </div>
  <p class="abs legal" style="left:328px;top:128px">All Rights Reserved</p>
  <p class="abs legal" style="left:588px;top:128px">Site Map | Privacy | Site Credits</p>
</footer>

</body>
</html>
```